Corvane Lift Inc Website Deisgn

We are a new small elevator contracting company.
We would like a full website designed similar to
http://pellusk-lifts.example or https://www.marbolt-hoistworks.example/
In addition to contents found on the above webpages.. we would like a section for project gallery etc.... have fun with it ... make it professional

Target Market(s)

Elevator Consultants - Property managers - Condo Boards - Commercial office buildings

Coding

Coded - Design and coding required

Number of Pages Required

5+ page

Requirements
Must have
• Navigation Bar.. Be view able via mobile ..Should be pictures of Tall Office buildings in background.. Toronto city skyline etc....

Have Fun!

```html
<!DOCTYPE html>
<html lang="en">
<head>
<meta charset="utf-8">
<title>Corvane Lift Inc</title>
<link href="https://fonts.googleapis.com/css2?family=Josefin+Sans:wght@300;400;600&display=swap" rel="stylesheet">
<style>
:root{
  --blue:#4a7bb7;
  --blue-dark:#3f6ea9;
  --heading:#4b7ab4;
  --ink:#1f1f1f;
  --muted:#9a9a9a;
  --line:#c9d4e3;
  --soft:#f4f4f4;
  --white:#ffffff;
}
*{box-sizing:border-box;margin:0;padding:0}
html,body{width:1200px;height:4049px;overflow:hidden}
body{position:relative;font-family:"Josefin Sans",sans-serif;font-weight:300;color:var(--ink);background:var(--white)}
.abs{position:absolute}
a{color:inherit;text-decoration:none}

/* header */
.social{left:118px;top:36px;display:flex;gap:12px}
.social span{width:26px;height:26px;border-radius:50%;background:var(--blue);display:block}
.brand{left:0;width:1200px;top:22px;text-align:center;font-size:44px;font-weight:600;color:var(--ink);letter-spacing:1px}
.top-contact{right:116px;top:30px;text-align:right;font-size:13px;line-height:22px}
.top-contact b{color:var(--blue);font-weight:400}

/* nav */
.nav{left:0;top:100px;width:1200px;height:50px;background:var(--blue);display:flex;justify-content:center;align-items:center;gap:42px}
.nav a{color:var(--white);font-size:14px;font-weight:400;letter-spacing:.5px;padding:6px 0;position:relative}
.nav a.active{font-weight:600}
.nav a.active::after{content:"";position:absolute;left:0;right:0;bottom:-10px;height:2px;background:var(--white)}

/* hero */
.hero{left:0;top:150px;width:1200px;height:356px;background:linear-gradient(180deg,#2c4a78 0%,#4b6a95 45%,#5d7ea7 70%,#2c3f5c 100%)}
.hero-small{left:0;width:1200px;top:222px;text-align:center;color:var(--white);font-size:30px}
.hero-title{left:0;width:1200px;top:262px;text-align:center;color:var(--white);font-size:62px;font-weight:400}
.btn{display:flex;align-items:center;justify-content:center;font-size:13px;font-weight:400}
.btn-white{background:var(--white);color:var(--blue)}
.btn-blue{background:var(--blue);color:var(--white)}

.banner{left:118px;top:466px;width:966px;height:147px;background:var(--blue);color:var(--white)}
.banner h2{position:absolute;left:34px;top:26px;font-size:34px;font-weight:400}
.banner p{position:absolute;left:34px;top:72px;font-size:20px;line-height:27px;width:760px}

/* section headings */
.sec-head{left:118px;width:966px;display:flex;align-items:center;gap:36px;font-size:48px;font-weight:400;color:var(--heading)}
.sec-head::before,.sec-head::after{content:"";flex:1;height:1px;background:var(--line)}
.sec-head.light{color:var(--white)}
.sec-head.light::before,.sec-head.light::after{background:rgba(255,255,255,.5)}
.lead{left:0;width:1200px;text-align:center;font-size:21px;font-weight:300}
.body-copy{font-size:12.5px;line-height:20px}

/* services */
.services{left:0;top:982px;width:1200px;height:492px;background:linear-gradient(135deg,#5c86bd 0%,#4a77b1 50%,#6a91c3 100%)}
.card{top:1136px;width:315px;height:269px;background:var(--white);text-align:center}
.card .icon{position:absolute;left:116px;top:22px;width:82px;height:82px;border-radius:50%;background:var(--blue)}
.card h3{position:absolute;left:0;right:0;top:125px;font-size:22px;font-weight:400;color:var(--heading)}
.card p{position:absolute;left:14px;right:14px;top:160px;font-size:12px;line-height:16.5px}
.card a{position:absolute;left:0;right:0;top:237px;font-size:12px;font-weight:600;color:var(--blue)}

/* feature */
.feature-title{left:118px;top:1668px;font-size:46px;font-weight:400;color:var(--heading)}
.feature-sub{left:118px;top:1734px;width:470px;font-size:20px;line-height:24px}
.feature-copy{left:118px;top:1800px;width:470px}
.photo{background:linear-gradient(135deg,#8a8f95,#c4c6c8 45%,#2e3440)}

/* gallery */
.gallery{left:0;top:2070px;width:1200px;height:790px;background:var(--soft)}
.tile{width:316px;height:267px}

/* form */
.field{height:18px;border-bottom:1px solid #d8d8d8;font-size:10px;color:var(--muted);padding-left:4px}

/* contact */
.contact{left:0;top:3346px;width:600px;height:398px;background:var(--blue);color:var(--white)}
.contact h2{position:absolute;left:118px;top:64px;font-size:48px;font-weight:400}
.contact p.intro{position:absolute;left:118px;top:133px;width:470px;font-size:11.5px;line-height:16px}
.contact dl{position:absolute;left:118px;top:220px;font-size:16px;line-height:34px}
.contact dt{display:inline;font-weight:600}
.contact dd{display:inline}
.map{left:600px;top:3346px;width:600px;height:398px;background:linear-gradient(160deg,#eef0e4,#dfe8d3 45%,#e9ecdf)}

/* footer */
.footer{left:0;top:3744px;width:1200px;height:247px;background:linear-gradient(180deg,#eceef1,#e3e6ea)}
.f-title{font-size:20px;font-weight:400;color:var(--heading)}
.f-links{font-size:16px;line-height:29px;font-weight:400;text-transform:uppercase}
.f-list{font-size:12px;line-height:21px;list-style:none}
.f-list li::before{content:"";display:inline-block;width:5px;height:5px;border-radius:50%;background:var(--blue);margin-right:9px;vertical-align:2px}
.copyright{left:0;top:3991px;width:1200px;height:58px;background:var(--blue);color:var(--white);font-size:13px;display:flex;align-items:center;justify-content:center}
</style>
</head>
<body>

<header>
  <div class="abs social" aria-label="Social links"><span></span><span></span><span></span></div>
  <div class="abs brand">Corvane Lift Inc</div>
  <div class="abs top-contact">
    <div><b>E-mail:</b> office@corvanelift.example</div>
    <div><b>Phone:</b> (555) 0142718 &nbsp;(555) 0199304</div>
  </div>
  <nav class="abs nav">
    <a class="active">HOME</a><a>ABOUT</a><a>SERVICES</a><a>CONSULTANTS</a><a>GALLERY</a><a>CONTACT</a>
  </nav>
</header>

<section>
  <div class="abs hero" role="img" aria-label="City skyline with tall office towers under a blue sky"></div>
  <div class="abs hero-small">Welcome To</div>
  <h1 class="abs hero-title">Corvane Lift Inc</h1>
  <a class="abs btn btn-white" style="left:551px;top:349px;width:97px;height:38px">Read More</a>
  <div class="abs banner">
    <h2>Lorem Ipsum Dolor</h2>
    <p>Sit amet, consectetur adipiscing elit, sed dempor incididunt ut labore et dolore magna Ut enim ad minim veniam,</p>
    <a class="btn btn-white" style="position:absolute;left:834px;top:56px;width:96px;height:38px">Free Quote</a>
  </div>
</section>

<section>
  <h2 class="abs sec-head" style="top:676px">About Us</h2>
  <p class="abs lead" style="top:750px">Lorem ipsum dolor sit amet, consectetur adipiscing elit, sed dempor</p>
  <p class="abs body-copy" style="left:170px;top:794px;width:860px;text-align:center">Lorem ipsum dolor sit amet, consectetur adipiscing elit, sed dempor incididunt ut labore et dolore magna aliqua. Ut enim ad minim veniam, quis nostrud exercitation ullamco laboris nisi ut aliquip ex ea commodo consequat.Lorem ipsum dolor sit amet, consectetur adipiscing elit, sed dempor incididunt ut labore et dolore magna aliqua. Ut enim ad minim veniam, quis nostrud exercitation ullamco laboris nisi ut aliquip ex ea commodo consequat.</p>
  <a class="abs btn btn-blue" style="left:551px;top:876px;width:97px;height:37px">Read More</a>
</section>

<section>
  <div class="abs services" role="img" aria-label="Glass office towers seen from below, tinted blue"></div>
  <h2 class="abs sec-head light" style="top:1042px">Services</h2>

  <article class="abs card" style="left:118px">
    <svg class="icon" viewBox="0 0 82 82"><circle cx="41" cy="41" r="41" fill="#4a7bb7"/><g fill="none" stroke="#fff" stroke-width="2"><rect x="27" y="22" width="28" height="38"/><path d="M32 28h4M39 28h4M46 28h4M32 35h4M39 35h4M46 35h4M32 42h4M39 42h4M46 42h4M37 60v-9h8v9"/></g></svg>
    <h3>Lorem Ipsum Dolor</h3>
    <p>Lorem ipsum dolor sit amet, consectetur adipiscing elit, sed dempor incididunt ut labore et dolore magna aliqua. Ut enim ad minim veniam quis nostrud exercitation ullamco laboris nisi</p>
    <a>Read More</a>
  </article>
  <article class="abs card" style="left:444px">
    <svg class="icon" viewBox="0 0 82 82"><circle cx="41" cy="41" r="41" fill="#4a7bb7"/><g fill="none" stroke="#fff" stroke-width="2"><rect x="27" y="21" width="26" height="40"/><path d="M40 25v36M33 25h14"/><circle cx="58" cy="38" r="1.5"/><circle cx="58" cy="44" r="1.5"/></g></svg>
    <h3>Lorem Ipsum Dolor</h3>
    <p>Lorem ipsum dolor sit amet, consectetur adipiscing elit, sed dempor incididunt ut labore et dolore magna aliqua. Ut enim ad minim veniam quis nostrud exercitation ullamco laboris nisi</p>
    <a>Read More</a>
  </article>
  <article class="abs card" style="left:769px">
    <svg class="icon" viewBox="0 0 82 82"><circle cx="41" cy="41" r="41" fill="#4a7bb7"/><g fill="none" stroke="#fff" stroke-width="2"><rect x="22" y="26" width="38" height="34" rx="3"/><rect x="27" y="36" width="7" height="18" rx="2"/><rect x="37" y="36" width="7" height="18" rx="2"/><rect x="47" y="36" width="7" height="18" rx="2"/><path d="M37 20h8M41 20v6"/></g></svg>
    <h3>Lorem Ipsum Dolor</h3>
    <p>Lorem ipsum dolor sit amet, consectetur adipiscing elit, sed dempor incididunt ut labore et dolore magna aliqua. Ut enim ad minim veniam quis nostrud exercitation ullamco laboris nisi</p>
    <a>Read More</a>
  </article>
</section>

<section>
  <h2 class="abs sec-head" style="top:1534px">Lorem Ipsum</h2>
  <h3 class="abs feature-title">Lorem Ipsum Dolor</h3>
  <p class="abs feature-sub">Lorem ipsum dolor sit amet, consectetur adipiscing elit, sed dempor incididunt</p>
  <p class="abs body-copy feature-copy">Lorem ipsum dolor sit amet, consectetur adipiscing elit, sed dempor incididunt ut labore et dolore magna aliqua. Ut enim ad minim veniam, quis nostrud exercitation ullamco laboris nisi ut aliquip ex ea commodo Lorem ipsum dolor sit amet, consectetur adipiscing elit, sed dempor incididunt ut labore et dolore magna aliqua. Ut enim ad minim veniam, quis nostrud</p>
  <a class="abs btn btn-blue" style="left:118px;top:1933px;width:96px;height:38px">Read More</a>
  <div class="abs photo" style="left:600px;top:1641px;width:484px;height:362px" role="img" aria-label="Businessman in a suit pressing an elevator call button"></div>
</section>

<section>
  <div class="abs gallery"></div>
  <h2 class="abs sec-head" style="top:2122px">Gallery</h2>
  <p class="abs lead" style="top:2190px">Lorem ipsum dolor sit amet, consectetur adipiscing elit, sed dempor</p>
  <div class="abs tile" style="left:118px;top:2242px;background:linear-gradient(135deg,#6f6d6a,#bdb8b0 55%,#d8cfc2)" role="img" aria-label="Stainless steel elevator doors in a stone lobby"></div>
  <div class="abs tile" style="left:442px;top:2242px;background:linear-gradient(135deg,#3f3c3a,#a9a49c 55%,#5a6a7a)" role="img" aria-label="Team meeting around a whiteboard in an office"></div>
  <div class="abs tile" style="left:766px;top:2242px;background:linear-gradient(135deg,#d7d4cf,#8c8278 55%,#2f3238)" role="img" aria-label="Consultant shaking hands with clients"></div>
  <div class="abs tile" style="left:118px;top:2528px;background:linear-gradient(135deg,#4a4744,#6b8fbf 50%,#9b7b5c)" role="img" aria-label="Man pressing an elevator button beside wooden panels"></div>
  <div class="abs tile" style="left:442px;top:2528px;background:linear-gradient(135deg,#2c2d30,#6e7073 55%,#b7b8b8)" role="img" aria-label="Two businessmen walking down office stairs"></div>
  <div class="abs tile" style="left:766px;top:2528px;background:linear-gradient(135deg,#2a3a55,#8aa0bd 50%,#c6a865)" role="img" aria-label="Glass panoramic elevators with brass frames"></div>
</section>

<section>
  <h2 class="abs sec-head" style="top:2918px">Free Quote</h2>
  <div class="abs field" style="left:118px;top:3038px;width:310px">Name :</div>
  <div class="abs field" style="left:445px;top:3038px;width:312px">Your Phone :</div>
  <div class="abs field" style="left:772px;top:3038px;width:312px">Your City :</div>
  <div class="abs field" style="left:118px;top:3106px;width:310px">Your Email :</div>
  <div class="abs field" style="left:445px;top:3106px;width:312px">Your Address :</div>
  <div class="abs field" style="left:772px;top:3106px;width:312px">Problem / Issues :</div>
  <div class="abs field" style="left:118px;top:3171px;width:966px">Your Message :</div>
  <a class="abs btn btn-blue" style="left:538px;top:3231px;width:121px;height:47px;font-size:15px">Submit Now</a>
</section>

<section>
  <div class="abs contact">
    <h2>Contact Us</h2>
    <p class="intro">Lorem ipsum dolor sit amet, consectetur adipiscing elit, sed dempor incididunt ut labore et dolore magna aliqua. Ut enim ad minim veniam, quis nostrud exercitation ullamco laboris nisi ut aliquip ex ea</p>
    <dl>
      <div><dt>Address:</dt> <dd>123,your text will come here your text will come here.</dd></div>
      <div><dt>E-mail:</dt> <dd>office@corvanelift.example</dd></div>
      <div><dt>Phone:</dt> <dd>(555) 0142718 , (555) 0199304</dd></div>
      <div><dt>Web:</dt> <dd>www.corvanelift.example</dd></div>
    </dl>
  </div>
  <div class="abs map" role="img" aria-label="Road map of the service region"></div>
</section>

<footer>
  <div class="abs footer" role="img" aria-label="Faint office towers in the background"></div>
  <h4 class="abs f-title" style="left:118px;top:3810px">Quick Links</h4>
  <div class="abs f-links" style="left:118px;top:3846px"><div style="font-weight:600">Home</div><div>About</div><div>Services</div></div>
  <div class="abs f-links" style="left:234px;top:3848px"><div>Consultants</div><div>Gallery</div><div>Contact</div></div>
  <h4 class="abs f-title" style="left:497px;top:3810px">Lorem Ipsum Dolor</h4>
  <ul class="abs f-list" style="left:497px;top:3848px"><li>Lorem ipsum dolor sit amet</li><li>consectetur adipiscing elit</li><li>sed dempor incididunt ut labore</li><li>et dolore magna aliqua Ut enim</li></ul>
  <h4 class="abs f-title" style="left:843px;top:3810px">Lorem Ipsum Dolor</h4>
  <p class="abs f-list" style="left:843px;top:3848px;width:250px">Lorem ipsum dolor sit amet, consectetur adipiscing elit, sed dempor incididunt ut labore et dolore magna aliqua. Ut enim ad minim veniam</p>
  <div class="abs copyright">Copyright © 2020 Corvane Lift Inc. All rights reserved.</div>
</footer>

</body>
</html>
```